Yard sign

Looking for a yard sign. <br/>Something simple, name, number. <br/>Large text, readable from 50 feet away. <br/><br/>18 x 24 inches.

Target Market(s)

Potential homeowners thinking about going solar.

Colors

Designer to choose colors to be used in the design.

Requirements
Must have
• "WE'VE GONE SOLAR!"
Nice to have
• We are a solar company, we would like a design that compliments the homeowners decision that they went solar and encourages others to do the same.

```html
<!DOCTYPE html>
<html lang="en">
<head>
<meta charset="utf-8">
<title>We've Gone Solar – Yard Sign</title>
<link rel="stylesheet" href="https://fonts.googleapis.com/css2?family=Montserrat:wght@700;800;900&display=swap">
<style>
  :root {
    --stage: #5f5f5f;
    --sky-top: #1a86c8;
    --sky-mid: #2f98d6;
    --sky-low: #7cc6ee;
    --panel-light: #3568b0;
    --panel-deep: #14245a;
    --panel-night: #101a44;
    --band-orange: #f4901e;
    --band-yellow: #fdc70c;
    --sun-yellow: #fbc01a;
    --brand-orange: #f39220;
    --white: #ffffff;
  }
  * { margin: 0; padding: 0; box-sizing: border-box; }
  html, body {
    width: 1200px; height: 955px; overflow: hidden;
    background: var(--stage);
    font-family: "Montserrat", Arial, sans-serif;
  }
  .yard-sign {
    position: absolute; left: 40px; top: 60px;
    width: 1120px; height: 836px; overflow: hidden;
    background: linear-gradient(180deg, var(--sky-top) 0%, var(--sky-mid) 45%, var(--sky-low) 85%);
  }
  .panel-field { position: absolute; inset: 0; width: 100%; height: 100%; }
  .headline {
    position: absolute; left: 0; right: 0; top: 88px;
    text-align: center; color: var(--white);
    font-weight: 900; line-height: 1; letter-spacing: -1px;
    text-shadow: 3px 4px 6px rgba(0, 30, 70, 0.45);
  }
  .headline-top { display: block; font-size: 101px; }
  .headline-main { display: block; font-size: 202px; margin-top: -6px; }
  .contact-band {
    position: absolute; left: 0; top: 661px; width: 770px; height: 117px;
    background: linear-gradient(90deg, var(--band-orange) 0%, var(--band-yellow) 45%, var(--band-orange) 100%);
  }
  .contact-band p {
    position: absolute; left: 66px; color: var(--white); font-weight: 700;
    text-shadow: 2px 3px 4px rgba(90, 40, 0, 0.45); white-space: nowrap;
  }
  .contact-phone { top: 10px; font-size: 44px; }
  .contact-web { top: 62px; font-size: 36px; }
  .brand {
    position: absolute; left: 738px; top: 625px;
    display: flex; align-items: center; gap: 16px;
  }
  .brand-dot {
    width: 104px; height: 104px; border-radius: 50%;
    background: var(--sun-yellow); flex: none;
  }
  .brand-name {
    color: var(--brand-orange); font-weight: 800;
    font-size: 50px; line-height: 1;
  }
</style>
</head>
<body>
  <main class="yard-sign">
    <svg class="panel-field" viewBox="0 0 1120 836" preserveAspectRatio="none" role="img" aria-label="Photo of rooftop solar panel rows angled against a blue sky">
      <defs>
        <linearGradient id="panelShade" x1="0" y1="0" x2="0.3" y2="1">
          <stop offset="0" stop-color="var(--panel-light)"/>
          <stop offset="0.55" stop-color="var(--panel-deep)"/>
          <stop offset="1" stop-color="var(--panel-night)"/>
        </linearGradient>
      </defs>
      <polygon points="0,340 1120,648 1120,836 0,836" fill="url(#panelShade)"/>
    </svg>

    <h1 class="headline">
      <span class="headline-top">WE'VE GONE</span>
      <span class="headline-main">SOLAR</span>
    </h1>

    <section class="contact-band">
      <p class="contact-phone">Call us 555-214-7890</p>
      <p class="contact-web">www.sunvalesolar.com</p>
    </section>

    <div class="brand">
      <span class="brand-dot"></span>
      <span class="brand-name">SUNVALE<br>SOLAR</span>
    </div>
  </main>
</body>
</html>
```